Create Lanternfield HR Business Cards.

Create Business Cards for Lanternfield HR. 2 sided and Would like the back to have the logo.

Info for Business Card:
Address: 4827 Millbrook Ave Suite 230 Cleveland, Ohio 44987
Office Number: 216-555-0143
Mobile: 216-555-0192

Website: www.lanternfieldhr.example

Target Market(s)

Small to medium size businesses

Industry/Entity Type

Human Resources

Contact Information for Business Card

Company logo and information

Font styles to use
Serif
Sans Serif

Requirements
Must have
• Info for Business Card: Address: 4827 Millbrook Ave Suite 230 Cleveland, Ohio 44987 Office Number: 216-555-0143 Mobile: 216-555-0192 Website: www.lanternfieldhr.example

```html
<!DOCTYPE html>
<html lang="en">
<head>
<meta charset="utf-8">
<title>Lanternfield HR Business Cards</title>
<link href="https://fonts.googleapis.com/css2?family=Poppins:wght@600;700&display=swap" rel="stylesheet">
<style>
  :root {
    --orange: #ea9236;
    --orange-deep: #e5862a;
    --navy: #3d3f6e;
    --white: #ffffff;
    --paper: #f1f1f1;
    --shadow: rgba(0, 0, 0, 0.12);
  }
  * { box-sizing: border-box; margin: 0; padding: 0; }
  html, body {
    width: 1200px;
    height: 1200px;
    overflow: hidden;
    background: var(--paper);
    font-family: "Poppins", sans-serif;
  }
  .sheet {
    width: 1200px;
    height: 1200px;
    display: flex;
    flex-direction: column;
    align-items: center;
    justify-content: center;
    gap: 70px;
  }
  .card {
    width: 860px;
    height: 492px;
    border-radius: 6px;
    overflow: hidden;
    box-shadow: 0 18px 40px var(--shadow);
  }
  /* Front */
  .card-front {
    background: linear-gradient(160deg, var(--orange) 0%, var(--orange-deep) 100%);
    display: flex;
    align-items: center;
    justify-content: center;
  }
  .brand {
    display: flex;
    align-items: center;
    gap: 22px;
    color: var(--navy);
    font-weight: 700;
  }
  .brand-dot {
    border-radius: 50%;
    background: var(--navy);
    flex: none;
  }
  .card-front .brand { font-size: 58px; }
  .card-front .brand-dot { width: 54px; height: 54px; }

  /* Back */
  .card-back { display: flex; }
  .back-brand {
    width: 40%;
    background: var(--white);
    display: flex;
    align-items: center;
    justify-content: center;
  }
  .back-brand .brand { font-size: 34px; gap: 14px; }
  .back-brand .brand-dot { width: 34px; height: 34px; background: var(--orange); }
  .back-info {
    width: 60%;
    background: linear-gradient(160deg, var(--orange) 0%, var(--orange-deep) 100%);
    padding: 62px 56px;
    display: flex;
    flex-direction: column;
    justify-content: center;
    gap: 30px;
    color: var(--white);
    font-weight: 600;
  }
  .info-row {
    display: flex;
    align-items: flex-start;
    gap: 20px;
  }
  .info-icon {
    width: 34px;
    height: 34px;
    flex: none;
    margin-top: 2px;
  }
  .info-text {
    font-size: 25px;
    line-height: 1.3;
  }
  .info-text.web { font-size: 21px; font-weight: 600; padding-top: 4px; }
</style>
</head>
<body>
<main class="sheet">

  <section class="card card-front" aria-label="Business card front">
    <div class="brand">
      <span class="brand-dot"></span>
      <span class="brand-name">Lanternfield HR</span>
    </div>
  </section>

  <section class="card card-back" aria-label="Business card back">
    <div class="back-brand">
      <div class="brand">
        <span class="brand-dot"></span>
        <span class="brand-name">Lanternfield HR</span>
      </div>
    </div>
    <div class="back-info">
      <div class="info-row">
        <svg class="info-icon" viewBox="0 0 34 34" aria-hidden="true">
          <circle cx="17" cy="17" r="17" fill="#ffffff" opacity="0.85"/>
          <path d="M17 8a6 6 0 0 0-6 6c0 4.5 6 11 6 11s6-6.5 6-11a6 6 0 0 0-6-6z" fill="none" stroke="#ea9236" stroke-width="2"/>
          <circle cx="17" cy="14" r="2" fill="#ea9236"/>
        </svg>
        <p class="info-text">4827 Millbrook Ave<br>Suite 230 Cleveland<br>Ohio 44987</p>
      </div>
      <div class="info-row">
        <svg class="info-icon" viewBox="0 0 34 34" aria-hidden="true">
          <circle cx="17" cy="17" r="17" fill="#ffffff" opacity="0.85"/>
          <path d="M12 9l3 0 1.5 4-2 1.5a9 9 0 0 0 4 4l1.5-2 4 1.5 0 3a2 2 0 0 1-2 2A13 13 0 0 1 10 11a2 2 0 0 1 2-2z" fill="#ea9236"/>
        </svg>
        <p class="info-text">216-555-0143<br>216-555-0192</p>
      </div>
      <div class="info-row">
        <svg class="info-icon" viewBox="0 0 34 34" aria-hidden="true">
          <circle cx="17" cy="17" r="17" fill="#ffffff" opacity="0.85"/>
          <circle cx="17" cy="17" r="8" fill="none" stroke="#ea9236" stroke-width="1.8"/>
          <ellipse cx="17" cy="17" rx="3.5" ry="8" fill="none" stroke="#ea9236" stroke-width="1.6"/>
          <line x1="9" y1="17" x2="25" y2="17" stroke="#ea9236" stroke-width="1.6"/>
        </svg>
        <p class="info-text web">www.lanternfieldhr.example</p>
      </div>
    </div>
  </section>

</main>
</body>
</html>
```